Silver Creek Plumbing Business card & letter head design

We need a new business card and letter head for our plumbing company called silver creek plumbing. attached is the companys logo. We provide domestic and commercial plumbing services in regional western Australia. We are after Something simple yet nice to look at and something that fits within the trade industry.

Target Market(s)

trade/building industry

Contact Information for Business Card

Darl Hensby
Manager
0461 238 574
enquiries@scplumbwork.net.au
ABN: 47 381 905 462
PCL: 5187

Domestic & Commercial Plumbing
Tip Truck & Excavator hire

Colors

Designer to choose colors to be used in the design.

```html
<!DOCTYPE html>
<html lang="en">
<head>
<meta charset="utf-8">
<title>Silver Creek Plumbing – Letterhead</title>
<link rel="stylesheet" href="https://fonts.googleapis.com/css2?family=Montserrat:wght@500;700;800&display=swap">
<style>
  :root {
    --navy: #1b2d5c;
    --blue: #1f8ad2;
    --sky: #dfeaf6;
    --paper: #ffffff;
    --footer-text: #ffffff;
  }
  * { margin: 0; padding: 0; box-sizing: border-box; }
  html, body { width: 849px; height: 1200px; overflow: hidden; background: var(--paper); }
  .letterhead {
    position: relative;
    width: 849px;
    height: 1200px;
    background: var(--paper);
    font-family: "Montserrat", Arial, sans-serif;
    overflow: hidden;
  }
  .brand {
    position: absolute;
    top: 44px;
    left: 60px;
    display: flex;
    align-items: center;
    gap: 14px;
  }
  .brand-dot {
    width: 26px;
    height: 26px;
    border-radius: 50%;
    background: var(--blue);
  }
  .brand-name {
    font-weight: 800;
    font-size: 30px;
    line-height: 1.05;
    letter-spacing: 0.5px;
    color: var(--navy);
    text-transform: uppercase;
  }
  .watermark {
    position: absolute;
    left: 50%;
    top: 595px;
    width: 300px;
    height: 300px;
    margin: -150px 0 0 -150px;
    border-radius: 50%;
    background: var(--sky);
    opacity: 0.55;
  }
  .footer-wave {
    position: absolute;
    left: 0;
    bottom: 0;
    width: 849px;
    height: 170px;
  }
  .footer-details {
    position: absolute;
    left: 70px;
    bottom: 30px;
    color: var(--footer-text);
    font-weight: 500;
    font-size: 17px;
    line-height: 1.55;
    letter-spacing: 0.3px;
  }
</style>
</head>
<body>
  <main class="letterhead">
    <header class="brand">
      <span class="brand-dot"></span>
      <span class="brand-name">Silver Creek<br>Plumbing</span>
    </header>

    <div class="watermark" aria-hidden="true"></div>

    <svg class="footer-wave" viewBox="0 0 849 170" preserveAspectRatio="none" aria-hidden="true">
      <path d="M0 40 C 220 110, 520 -10, 849 30 L 849 170 L 0 170 Z" fill="var(--blue)"/>
      <path d="M0 62 C 240 125, 540 20, 849 52 L 849 170 L 0 170 Z" fill="var(--navy)"/>
    </svg>

    <footer class="footer-details">
      <p>Email: enquiries@scplumbwork.net.au</p>
      <p>ABN: 47 381 905 462, PCL: 5187</p>
    </footer>
  </main>
</body>
</html>
```